Create a Brochure Design for Harlow Senior Living

Harlow Senior Living is a subsidiary of the Harlow Care Group. This brochure is specifically for the Harlow Senior Living company and brand. Create a 3 panel, front and back, tri-fold brochure. This brochure will be a way to introduce our senior living care home to the community, prospective, clients, and various referral partners. It is modern and state of the art home. Like the home, the brochure must be eye catching, unique in its deliverables (as it doesn’t feel like a care facility) and demonstrate both attention to detail and comfort. Our organization is sophisticated and built around warmth, care and individualized personal attention. The most important aspect of this design is to focus on creating a nurturing, warm, and inviting feel where you would want to put your own loved ones in our care home.
I am open to the creativity of the designer to develop something based on the above criteria; however I would like the design to work well with the existing collateral material. What I mean by that is that while I want everything to have its own personality and stand out as its own brand representative, I still need to be able to tell that the overall design concept stays stylistically inside of the same ‘family’ of existing designed material. Because of this, below I would like for the designer to pull inspiration from the link to our website (Located below) as well as from the attachment of our recently refreshed business cards (Attached). This should allow each design to be unique and creative, while still staying inside of a framework and the feel/style that I am looking for.
Finally, I want all the designers to understand that this brochure design is for a facility where we are responsible to provide care for active, positive, and happy seniors/elders. We have care professionals and staff on-site to provide 24x7, around the clock, care to the elders and geriatric residents as it is needed and required. The photos that are used must represent aging gracefully and with elegance.
Target Market(s)
Seniors(50+), Caring Family Members, Social Workers, Physicians, Hospitals
Industry/Entity Type
Business
Requirements
Must have
- • The company logo must be included.
Nice to have
- Attached you will find a sampling of images related to the long term care industry. Please feel free to use your own images as you see fit. The interior care home pictures are of our actual facility and should be incorporated into the brochure and your design.
Company Information
• Look under the Harlow Senior Living tab at
www.harlowcaregroup.example.

```html
<!DOCTYPE html>
<html lang="en">
<head>
<meta charset="utf-8">
<title>Harlow Senior Living – Tri-fold Brochure</title>
<link href="https://fonts.googleapis.com/css2?family=Fira+Sans:wght@400;500;600;700&display=swap" rel="stylesheet">
<style>
  :root {
    --teal: #4f9b98;
    --teal-light: #63a9a6;
    --teal-dark: #3f8784;
    --white: #ffffff;
    --silver-1: #f2f2f2;
    --silver-2: #a9a9a9;
    --silver-3: #dcdcdc;
    --stage: #c4c4c4;
    --ink: #4a4a4a;
  }
  * { box-sizing: border-box; margin: 0; padding: 0; }
  html, body { width: 1200px; height: 863px; overflow: hidden; }
  body {
    background: var(--stage);
    font-family: "Fira Sans", Arial, sans-serif;
    position: relative;
  }

  .brochure-inside, .brochure-cover {
    position: absolute;
    top: 131px;
    height: 600px;
    background: var(--white);
    overflow: hidden;
    box-shadow: 0 6px 18px rgba(0,0,0,0.18);
  }
  .brochure-inside { left: 50px; width: 780px; }
  .brochure-cover { left: 890px; width: 260px; }

  .silver-band {
    position: absolute; left: 0; right: 0; height: 12px;
    background: linear-gradient(90deg, var(--silver-2), var(--silver-1) 30%, var(--silver-3) 60%, var(--silver-2));
  }
  .silver-band.top { top: 0; }
  .silver-band.bottom { bottom: 0; }

  .teal-rule { position: absolute; left: 0; right: 0; height: 3px; background: var(--teal); }

  /* Brand name block */
  .brand {
    position: absolute;
    display: flex; flex-direction: column; align-items: center; gap: 6px;
    color: var(--teal-dark);
    font-weight: 500;
    text-align: center;
  }
  .brand-mark { width: 18px; height: 18px; background: var(--teal); }
  .brand-name { font-size: 17px; line-height: 1.15; }

  /* Inside spread */
  .inside-header .brand { left: 0; width: 260px; top: 38px; }
  .tagline {
    position: absolute; left: 560px; top: 50px; width: 180px;
    font-size: 8px; letter-spacing: 1.5px; line-height: 1.5;
    color: var(--teal); text-transform: uppercase;
  }

  .photo { position: absolute; }
  .photo-bedroom {
    left: 0; top: 138px; width: 260px; height: 200px;
    background: linear-gradient(160deg, #d9cdb2 0%, #9c7b55 45%, #5a3d28 100%);
  }
  .photo-lounge {
    left: 262px; top: 138px; width: 258px; height: 200px;
    background: linear-gradient(170deg, #e8dcc2 0%, #b18a5a 50%, #6d5238 100%);
  }
  .photo-bathroom {
    left: 522px; top: 112px; width: 258px; height: 200px;
    background: linear-gradient(165deg, #f2ece0 0%, #cdbb98 55%, #8e6f4a 100%);
  }

  .feature-badge {
    position: absolute; width: 68px; height: 68px; border-radius: 50%;
    background: var(--teal); border: 3px solid var(--white);
    color: var(--white); font-size: 8px; font-weight: 600; line-height: 1.2;
    display: flex; align-items: center; justify-content: center; text-align: center;
    padding: 8px;
  }
  .badge-bedrooms { left: 205px; top: 305px; }
  .badge-lounge { left: 460px; top: 110px; }
  .badge-bathrooms { left: 712px; top: 140px; }

  .content-panels { position: absolute; left: 0; top: 340px; width: 780px; height: 248px; display: flex; }
  .content-panel { width: 260px; height: 100%; padding: 34px 24px 0 26px; color: var(--white); }
  .content-panel.left { background: var(--teal); }
  .content-panel.middle { background: var(--teal-light); }
  .content-panel.right { background: var(--teal); }
  .content-panel h2 { font-size: 14px; font-weight: 700; line-height: 1.2; margin-bottom: 10px; }
  .content-panel .lead { font-size: 9.5px; font-weight: 600; line-height: 1.45; margin-bottom: 12px; }
  .content-panel .note { font-size: 8.5px; line-height: 1.5; color: rgba(255,255,255,0.72); }
  .content-panel.right { padding-top: 0; }
  .right-copy { position: absolute; left: 546px; top: 322px; width: 210px; color: var(--white); }
  .right-copy h2 { font-size: 14px; font-weight: 700; line-height: 1.2; margin-bottom: 10px; }
  .right-copy .lead { font-size: 9.5px; font-weight: 600; line-height: 1.45; margin-bottom: 12px; }
  .right-copy .note { font-size: 8.5px; line-height: 1.5; color: rgba(255,255,255,0.72); }
  .right-panel-fill { position: absolute; left: 520px; top: 312px; width: 260px; height: 28px; background: var(--teal); }

  .fold { position: absolute; top: 12px; bottom: 12px; width: 2px; background: rgba(255,255,255,0.9); }
  .fold-1 { left: 260px; }
  .fold-2 { left: 520px; }

  /* Cover */
  .cover-header .brand { left: 0; width: 260px; top: 62px; }
  .cover-rule-1 { top: 196px; }
  .cover-rule-2 { top: 202px; height: 1px; }
  .photo-couple {
    left: 0; top: 206px; width: 260px; height: 382px;
    background: linear-gradient(180deg, #dbe7f0 0%, #c9d9e4 45%, #e8d6c6 75%, #f1ece6 100%);
  }
</style>
</head>
<body>

<section class="brochure-inside" aria-label="Inside spread">
  <div class="silver-band top"></div>

  <header class="inside-header">
    <div class="brand">
      <span class="brand-mark"></span>
      <span class="brand-name">Harlow<br>Senior Living</span>
    </div>
    <p class="tagline">Experience life like you always hoped it could be</p>
  </header>

  <div class="teal-rule" style="top:134px;width:520px;"></div>
  <div class="teal-rule" style="top:108px;left:520px;"></div>

  <div class="photo photo-bedroom" role="img" aria-label="Resident bedroom with bed, dark wood furniture and garden window"></div>
  <div class="photo photo-lounge" role="img" aria-label="Open lounge with sofas, rug and warm lighting"></div>
  <div class="photo photo-bathroom" role="img" aria-label="Bright accessible bathroom with walk-in shower"></div>
  <div class="right-panel-fill"></div>

  <div class="content-panels">
    <article class="content-panel left">
      <h2>Lorem ipsum dolor sit amet at nostrum definitions</h2>
      <p class="lead">Ponderum periculis moderatius et per. Te eos mundi accusam oblaborum, mel ea reque ubi, eu homi option mel. Ei usu paulo animal signiferumque. Tempor hendrerit aliquando ex duo, vidit democritum mei te, id diam semper timeam his.</p>
      <p class="note">Quo nibh porro an, vim ut mazim dicant utamur. Sea ne quod viris eleifend, nam at tale iusto.</p>
    </article>
    <article class="content-panel middle">
      <h2>Lorem ipsum dolor sit amet at nostrum definitions</h2>
      <p class="lead">Ponderum periculis moderatius et per. Te eos mundi accusam oblaborum, mel ea reque ubi, eu homi option mel. Ei usu paulo animal signiferumque. Tempor hendrerit aliquando ex duo, vidit democritum mei te, id diam semper timeam his.</p>
      <p class="note">Vel an graeci mentitum, duo ut nostro inermis. Eam at probo zril, ius ea quas error.</p>
    </article>
    <article class="content-panel right"></article>
  </div>

  <div class="right-copy">
    <h2>Lorem ipsum dolor sit amet at nostrum definitions</h2>
    <p class="lead">Ponderum periculis moderatius et per. Te eos mundi accusam oblaborum, mel ea reque ubi, eu homi option mel. Ei usu paulo animal signiferumque. Tempor hendrerit aliquando ex duo, vidit democritum mei te, id diam semper timeam his.</p>
    <p class="note">Mei cu alii nusquam, has ne velit dicta. Id his oratio legimus, duo id odio dolor.</p>
  </div>

  <div class="feature-badge badge-bedrooms">Comfortable Bedrooms</div>
  <div class="feature-badge badge-lounge">Spacious Lounge Areas</div>
  <div class="feature-badge badge-bathrooms">Spacious Bathrooms</div>

  <div class="fold fold-1"></div>
  <div class="fold fold-2"></div>

  <div class="silver-band bottom"></div>
</section>

<section class="brochure-cover" aria-label="Front cover">
  <div class="silver-band top"></div>
  <header class="cover-header">
    <div class="brand">
      <span class="brand-mark"></span>
      <span class="brand-name">Harlow<br>Senior Living</span>
    </div>
  </header>
  <div class="teal-rule cover-rule-1"></div>
  <div class="teal-rule cover-rule-2"></div>
  <div class="photo photo-couple" role="img" aria-label="Smiling senior couple embracing outdoors against a pale sky"></div>
  <div class="silver-band bottom"></div>
</section>

</body>
</html>
```